Mercedes Metris Cargo Van

Need a simple design includes company logo, website, phone number and listing of our IT services.
Need to have company logo on right, left and back sides,
Website listed: corvalink.net
Phone number: 555-316-4827
QR code
I would like the following:
IT Services
Wi-Fi
Cabling
Security Cameras
Access Control

Target Market(s)

Local companies

Industry/Entity Type

IT Consultants and Cabling

Font styles to use
Sans Serif

Requirements
Must have
• Logo, website: corvalink.net , phone: 555-316-4827, services

```html
<!DOCTYPE html>
<html lang="en">
<head>
<meta charset="utf-8">
<title>CorvaLink Van Wrap</title>
<link href="https://fonts.googleapis.com/css2?family=Oswald:wght@400;500;600&display=swap" rel="stylesheet">
<style>
  :root {
    --stage: #1c1c1c;
    --body-grey: #4a4948;
    --body-dark: #2e2d2d;
    --glass: #3a3a3a;
    --wrap-white: #ffffff;
    --brand-red: #d7121f;
    --brand-red-deep: #a30d17;
    --band-grey: #5c5b5b;
    --ink: #161616;
  }
  * { margin: 0; padding: 0; box-sizing: border-box; }
  html, body { width: 1200px; height: 296px; overflow: hidden; background: var(--stage); }
  .canvas { position: relative; width: 1200px; height: 296px; font-family: "Oswald", sans-serif; }
  .wrap-shapes { position: absolute; inset: 0; }
  .rot { position: absolute; transform-origin: left center; white-space: nowrap; }

  .side-wordmark { left: 262px; top: 160px; transform: rotate(-14deg); font-size: 64px; font-weight: 500; color: var(--ink); letter-spacing: 1px; line-height: 1; }

  .side-contact { left: 92px; top: 170px; transform: rotate(-14deg); display: flex; flex-direction: column; align-items: flex-start; gap: 3px; }
  .band { display: block; font-weight: 600; color: var(--wrap-white); letter-spacing: 1px; line-height: 1; }
  .side-contact .phone-band { background: var(--band-grey); font-size: 16px; padding: 3px 18px 3px 8px; clip-path: polygon(0 0, 100% 0, 94% 100%, 0 100%); }
  .side-contact .web-band { background: var(--brand-red); font-size: 14px; padding: 3px 18px 3px 40px; clip-path: polygon(0 0, 100% 0, 94% 100%, 0 100%); }

  .side-services { transform: rotate(-14deg); font-size: 9px; font-weight: 500; color: var(--ink); line-height: 1.15; list-style: none; }
  .side-services li::before { content: ""; display: inline-block; width: 3px; height: 3px; border-radius: 50%; background: var(--brand-red); margin-right: 4px; vertical-align: middle; }
  .side-services.col-a { left: 346px; top: 100px; }
  .side-services.col-b { left: 406px; top: 80px; }

  .back-wordmark { position: absolute; left: 0; width: 100%; padding-left: 990px; padding-right: 210px; top: 38px; font-size: 36px; font-weight: 400; color: var(--wrap-white); line-height: 1; text-align: center; }
  .back-services { position: absolute; left: 988px; top: 152px; list-style: none; font-size: 5.5px; font-weight: 500; color: var(--ink); line-height: 1.1; }
  .back-services li::before { content: ""; display: inline-block; width: 2px; height: 2px; border-radius: 50%; background: var(--brand-red); margin-right: 3px; vertical-align: middle; }
  .back-contact { position: absolute; left: 880px; top: 190px; display: flex; flex-direction: column; align-items: flex-start; gap: 1px; }
  .back-contact .phone-band { margin-left: 30px; background: var(--band-grey); font-size: 13px; padding: 2px 30px 2px 10px; clip-path: polygon(4% 0, 100% 0, 100% 100%, 0 100%); letter-spacing: 0.5px; }
  .back-contact .web-band { background: var(--brand-red); font-size: 13px; padding: 2px 40px 2px 10px; clip-path: polygon(3% 0, 100% 0, 95% 100%, 0 100%); letter-spacing: 0.5px; }
</style>
</head>
<body>
<main class="canvas">
  <svg class="wrap-shapes" viewBox="0 0 1200 296" width="1200" height="296" aria-hidden="true">
    <g class="side-panel">
      <path d="M40 150 Q60 110 120 100 L240 40 Q260 24 300 22 L690 22 Q725 24 730 70 L738 200 Q740 235 720 240 L50 240 Q30 230 32 190 Z" fill="var(--body-grey)"/>
      <path d="M215 60 L325 38 L325 105 L200 112 Z" fill="var(--glass)"/>
      <path d="M350 34 L690 34 Q710 36 712 80 L712 100 L350 104 Z" fill="var(--body-dark)" opacity="0.5"/>
      <path d="M80 160 Q120 120 200 112 L330 104 Q420 60 540 50 Q640 46 640 80 Q630 150 470 210 Q400 232 340 236 L60 236 Q40 210 80 160 Z" fill="var(--wrap-white)"/>
      <path d="M390 60 Q520 40 620 50 Q650 60 640 90 Q620 160 470 216 Q420 232 360 236 L430 232 Q560 200 612 130 Q640 80 600 64 Q520 52 390 60 Z" fill="var(--brand-red)"/>
      <circle cx="135" cy="230" r="38" fill="var(--body-dark)"/>
      <circle cx="135" cy="230" r="28" fill="#b9b9b9"/>
      <circle cx="600" cy="230" r="38" fill="var(--body-dark)"/>
      <circle cx="600" cy="230" r="28" fill="#b9b9b9"/>
    </g>
    <g class="back-panel">
      <path d="M860 30 Q870 14 900 14 L1085 14 Q1112 14 1120 30 L1134 240 Q1134 262 1112 262 L866 262 Q846 262 846 240 Z" fill="var(--body-grey)"/>
      <path d="M878 28 L1102 28 Q1108 30 1108 40 L1104 100 Q1100 106 1092 106 L888 106 Q880 106 878 98 Z" fill="var(--body-dark)" opacity="0.6"/>
      <path d="M870 240 L870 160 Q880 118 960 108 Q1050 100 1080 130 Q1092 180 1060 240 Z" fill="var(--wrap-white)"/>
      <path d="M890 126 Q960 96 1040 104 Q1080 112 1078 150 Q1072 210 1040 240 L1060 240 Q1098 200 1096 144 Q1094 110 1050 100 Q960 92 890 126 Z" fill="var(--brand-red)"/>
      <rect x="846" y="110" width="14" height="60" rx="3" fill="var(--brand-red-deep)"/>
      <rect x="1120" y="110" width="14" height="60" rx="3" fill="var(--brand-red-deep)"/>
    </g>
  </svg>

  <div class="rot side-contact">
    <span class="band phone-band">555-316-4827</span>
    <span class="band web-band">CORVALINK.NET</span>
  </div>
  <ul class="rot side-services col-a">
    <li>IT SERVICES</li><li>WI-FI</li><li>CABLING</li>
  </ul>
  <ul class="rot side-services col-b">
    <li>SECURITY CAMERAS</li><li>ACCESS CONTROL</li>
  </ul>
  <div class="rot side-wordmark">CorvaLink</div>

  <div class="back-wordmark">CorvaLink</div>
  <ul class="back-services">
    <li>IT SERVICES</li><li>WI-FI</li><li>CABLING</li><li>SECURITY CAMERAS</li><li>ACCESS CONTROL</li>
  </ul>
  <div class="back-contact">
    <span class="band phone-band">555-316-4827</span>
    <span class="band web-band">CORVALINK.NET</span>
  </div>
</main>
</body>
</html>
```